Need modern simple design for magazine ad, apartment and condo roofer.

I need a half page magazine ad for a local roofer to publish in an industry magazine. Apartment associations industry. All types of roofs. Shingle and Flat
Need the design to be creative and modern, clean and simple. I do not want a busy design. One that stands out and makes a point quickly.
Logo must be prominent.
DO NOT USE PHOTOS FROM MY WEBSITE PLEASE. Looking for something new.
I work on entire complexes not houses.

Need to make sure our phone number and email address are listed at the bottom. Here is my website www.vorbelan.com
Want to stay away from standard clip arts of tools, homes, apartment buildings.
Half Horizontal 7.25 x 4.75
Ads should be in PDF and JPG format.

Target Market(s)

Apartment or Condo owners looking for large scale roofing projects

Industry/Entity Type

Roofing

Requirements
Must have
• Prominent Logo
Simple Clean Design
Create graphics
Not Busy
Should not have
• Clip Art
No Photos from my website

```html
<!DOCTYPE html>
<html lang="en">
<head>
<meta charset="utf-8">
<title>Vorbelan Roofing – Half Page Ad</title>
<link rel="stylesheet" href="https://fonts.googleapis.com/css2?family=Roboto+Condensed:ital,wght@0,700;0,800;1,900&family=Roboto:wght@500&display=swap">
<style>
  :root {
    --mat: #292826;
    --paper: #ffffff;
    --brand-blue: #2c6fb0;
    --headline: #ffffff;
    --accent-yellow: #f5c400;
    --ink: #2b2b2b;
    --footer-grey: #d1cfce;
    --facade-top: #b9674a;
    --facade-mid: #cfa45c;
    --facade-low: #b88c48;
  }
  * { margin: 0; padding: 0; box-sizing: border-box; }
  html, body { width: 1200px; height: 855px; overflow: hidden; }
  body { background: var(--mat); position: relative; font-family: "Roboto Condensed", Arial, sans-serif; }

  .ad {
    position: absolute; left: 88px; top: 92px;
    width: 1023px; height: 670px;
    background: var(--paper); overflow: hidden;
  }
  .blue-field { position: absolute; left: 0; top: 0; width: 1023px; height: 551px; }

  .facades {
    position: absolute; left: 0; top: 330px; width: 1023px; height: 221px;
    background: linear-gradient(180deg, var(--facade-top) 0%, var(--facade-mid) 22%, var(--facade-mid) 70%, var(--facade-low) 100%);
  }

  .brand {
    position: absolute; left: 20px; top: 46px;
    display: flex; align-items: center; gap: 12px;
  }
  .brand-mark { width: 30px; height: 30px; background: var(--brand-blue); }
  .brand-name {
    font-family: "Roboto Condensed", Arial, sans-serif;
    font-weight: 800; font-size: 48px; line-height: 1;
    color: var(--brand-blue); letter-spacing: -0.5px;
  }

  .services {
    position: absolute; left: 122px; top: 145px;
    list-style: none;
    font-family: "Roboto", Arial, sans-serif; font-weight: 500;
    font-size: 15px; line-height: 18.8px; color: var(--ink);
  }
  .services li { position: relative; padding-left: 16px; }
  .services li::before {
    content: ""; position: absolute; left: 0; top: 5px;
    width: 8px; height: 8px; background: var(--brand-blue);
  }
  .services li.more::before { display: none; }

  .headline {
    position: absolute; left: 0; top: 0;
    font-weight: 900; font-style: italic; font-size: 98px;
    line-height: 75px; color: var(--headline); letter-spacing: -1px;
    text-transform: uppercase;
  }
  .headline span { position: absolute; white-space: nowrap; }
  .headline .l1 { left: 460px; top: 30px; }
  .headline .l2 { left: 430px; top: 105px; }
  .headline .l3 { left: 413px; top: 180px; }

  .tagline {
    position: absolute; left: 402px; top: 266px;
    font-weight: 700; font-size: 32px; color: var(--accent-yellow);
    white-space: nowrap; letter-spacing: -0.2px;
  }

  .contact-bar {
    position: absolute; left: 0; top: 551px; width: 1023px; height: 119px;
    background: var(--footer-grey); color: var(--ink);
  }
  .contact-item { position: absolute; display: flex; align-items: center; white-space: nowrap; font-weight: 700; }
  .icon { display: block; flex: none; }
  .address { left: 142px; top: 14px; font-size: 30px; gap: 12px; }
  .phone { left: 95px; top: 50px; font-size: 52px; gap: 14px; }
  .email { left: 454px; top: 50px; font-size: 52px; gap: 12px; }
</style>
</head>
<body>
  <section class="ad">
    <svg class="blue-field" viewBox="0 0 1023 551" aria-hidden="true">
      <polygon points="457,0 1023,0 1023,551 255,551" fill="#2c6fb0"/>
    </svg>

    <div class="facades" role="img" aria-label="Photograph of a row of old multi-storey apartment buildings with terracotta roofs and shuttered windows"></div>

    <div class="brand">
      <span class="brand-mark"></span>
      <span class="brand-name">Vorbelan Roofing</span>
    </div>

    <ul class="services">
      <li>Exterior Renovations</li>
      <li>Interior Renovations</li>
      <li>Disaster Restoration</li>
      <li>Balcony/Landing Repairs</li>
      <li>Brick/Stucco/Masonry</li>
      <li>Carports / Metal Fencing</li>
      <li>Full Paint</li>
      <li class="more">and more. . .</li>
    </ul>

    <h1 class="headline">
      <span class="l1">Apartment</span>
      <span class="l2">Associations</span>
      <span class="l3">Industry</span>
    </h1>

    <p class="tagline">All types of roofs. Shingle And Flat</p>

    <footer class="contact-bar">
      <div class="contact-item address">
        <svg class="icon" width="30" height="30" viewBox="0 0 30 30" aria-hidden="true">
          <circle cx="15" cy="15" r="15" fill="#2c6fb0"/>
          <path d="M15 7a5 5 0 0 0-5 5c0 4 5 9 5 9s5-5 5-9a5 5 0 0 0-5-5z" fill="none" stroke="#fff" stroke-width="1.8"/>
          <circle cx="15" cy="12" r="1.8" fill="#fff"/>
          <path d="M9 23h12" stroke="#fff" stroke-width="1.8"/>
        </svg>
        <span>214 Larkspur Avenue, Suite 300 Dunmore, TX 75990</span>
      </div>
      <div class="contact-item phone">
        <svg class="icon" width="36" height="36" viewBox="0 0 36 36" aria-hidden="true">
          <circle cx="18" cy="18" r="18" fill="#2c6fb0"/>
          <rect x="12" y="8" width="12" height="20" rx="2" fill="none" stroke="#fff" stroke-width="2"/>
          <circle cx="18" cy="24.5" r="1.2" fill="#fff"/>
        </svg>
        <span>555.014.2837</span>
      </div>
      <div class="contact-item email">
        <svg class="icon" width="34" height="34" viewBox="0 0 34 34" aria-hidden="true">
          <circle cx="17" cy="17" r="17" fill="#2c6fb0"/>
          <rect x="8" y="11" width="18" height="12" rx="1" fill="none" stroke="#fff" stroke-width="1.8"/>
          <path d="M8 11l9 7 9-7" fill="none" stroke="#fff" stroke-width="1.8"/>
        </svg>
        <span>info@vorbelan.com</span>
      </div>
    </footer>
  </section>
</body>
</html>
```